Killer Online Marketing Company Needs Sweet Methodology Graphic Created!

We need a totally sweet custom methodology graphic created for a new Online Marketing Company from Phoenix Arizona called BRISK Online Marketing. We outsource and automate online, social media, and mobile marketing for small to medium businesses. Our services create more leads, more sales, and fewer headaches for our clients when it comes to managing their online marketing systems.

Our methodology graphic will be used in videos, web, print, and everywhere we go to explain how we work with clients. Our methodology is based on our name STEAM:

STRATEGIZE
TARGET
ENGAGE
AUTOMATE
MONETIZE

It needs to fit in with our overall brand look/feel which a cool future retro transportation theme. We aren't some stuffy QLX/Cubicle Hours TPS report loving desk jockeys. We are hardcore marketers who love making an impact. When everyone goes high-tech we go retro. If you've got a wicked design sense and get our retro-future vibe... please submit.

See the attached company logos to see what we are all about. If you are the winning designer, we will absolutely be using you more into the future as this is just the beginning and we're already busier than a bunch of one-legged men in a butt-kicking competition.
Updates

Just for clarities sake, we want this to be the following;

A) A stand alone graphic (no backgrounds) because this will be used in various applications with different backgrounds.

B) A lifecycle with a clear relationship from one step the the next that is repeated over and over. Thus the word "cycle". See some examples of cool methodology graphics below that we like (in no particular order):

3. Harborline Group (really like the feel of this one)
4. Mid.Motion.Craft
5. Quillwork Software (this one has a cool feel as well)
6. Brevo (this one rocks)
7. Tandrel Systems (very clean)
8. Pemvora Technology (a little too techy, but interesting use of arrows)

Hopefully these give some inspiration and clarification.

Thanks,
Daniel Frayne

Target Market(s)

GenX and Baby Boomer Business Owners, entrepreneurs, marketing managers, dancing cat trainers (just kidding)

Industry/Entity Type

Marketing

Requirements
Must have
• 1. It must include the stages of our service lifecycle methodology
2. It must illustrate the flow from stage to stage
3. It must match the retro-future feel of our brand
4. It must be usable in both web, print, and video
5. It must be iconic enough that it can stand alone as a graphic
Nice to have
• 1. A slight 3D quality to give the design some depth would be cool (we think... you're the designer... surprise us)
2. Presentable in both full color version and black/white/grayscale version.
3. It needs to connect with both our brand, but also the theme of online, social media, and mobile marketing
4. If you were walking by this on a poster.. it should make you stop and go... That's sweet, what's that all about!
Should not have
• 1. Nothing overtly cartoony. We went with retro future images, but didn't want them to be cartoony. We want cool retro future mod.

```html
<!DOCTYPE html>
<html lang="en">
<head>
<meta charset="utf-8">
<title>BRISK Online Marketing — Methodology Cycle</title>
<link rel="stylesheet" href="https://fonts.googleapis.com/css2?family=Josefin+Sans:wght@400&display=swap">
<style>
  :root {
    --canvas-bg: #ffffff;
    --disc-light: #9a9a9a;
    --disc-mid: #7a7a7a;
    --disc-dark: #555555;
    --rim: #4a4a4a;
    --hub-light: #4a4a4a;
    --hub-dark: #262626;
    --arrow-dark: #3b3b3b;
    --arrow-accent: #8e1b1b;
    --label: #ffffff;
  }
  html, body {
    margin: 0;
    padding: 0;
    width: 1200px;
    height: 849px;
    overflow: hidden;
    background: var(--canvas-bg);
  }
  .methodology-cycle {
    display: block;
    width: 1200px;
    height: 849px;
  }
  .stage-label {
    font-family: "Josefin Sans", sans-serif;
    font-weight: 400;
    font-size: 42px;
    letter-spacing: 4px;
    fill: var(--label);
    text-anchor: middle;
    dominant-baseline: central;
  }
  .brand-name {
    font-family: "Josefin Sans", sans-serif;
    font-weight: 400;
    fill: var(--label);
    text-anchor: middle;
  }
  .brand-name--primary { font-size: 92px; letter-spacing: 6px; }
  .brand-name--secondary { font-size: 28px; letter-spacing: 3px; }
</style>
</head>
<body>
<svg class="methodology-cycle" viewBox="0 0 1200 849" xmlns="http://www.w3.org/2000/svg" aria-labelledby="cycle-title">
  <title id="cycle-title">BRISK methodology: Strategize, Target, Engage, Automate, Monetize</title>
  <defs>
    <radialGradient id="disc-fill" cx="45%" cy="35%" r="70%">
      <stop offset="0%" stop-color="var(--disc-light)"/>
      <stop offset="60%" stop-color="var(--disc-mid)"/>
      <stop offset="100%" stop-color="var(--disc-dark)"/>
    </radialGradient>
    <radialGradient id="hub-fill" cx="50%" cy="40%" r="60%">
      <stop offset="0%" stop-color="var(--hub-light)"/>
      <stop offset="100%" stop-color="var(--hub-dark)"/>
    </radialGradient>
    <filter id="soft-shadow" x="-10%" y="-10%" width="120%" height="120%">
      <feDropShadow dx="3" dy="5" stdDeviation="5" flood-color="#000" flood-opacity="0.45"/>
    </filter>
    <filter id="label-shadow">
      <feDropShadow dx="2" dy="2" stdDeviation="1.5" flood-color="#000" flood-opacity="0.6"/>
    </filter>
  </defs>

  <g class="cycle-disc" filter="url(#soft-shadow)">
    <ellipse cx="612" cy="425" rx="462" ry="410" fill="var(--rim)"/>
    <ellipse cx="612" cy="425" rx="450" ry="398" fill="url(#disc-fill)"/>
  </g>

  <g class="cycle-arrows" filter="url(#soft-shadow)">
    <polygon class="cycle-arrow cycle-arrow--start" fill="var(--arrow-accent)" points="40,0 -30,-50 -30,50" transform="translate(345 198) rotate(40)"/>
    <polygon class="cycle-arrow" fill="var(--arrow-dark)" points="40,0 -30,-50 -30,50" transform="translate(748 150) rotate(25)"/>
    <polygon class="cycle-arrow" fill="var(--arrow-dark)" points="40,0 -30,-50 -30,50" transform="translate(965 420) rotate(95)"/>
    <polygon class="cycle-arrow" fill="var(--arrow-dark)" points="40,0 -30,-50 -30,50" transform="translate(728 712) rotate(160)"/>
    <polygon class="cycle-arrow" fill="var(--arrow-dark)" points="40,0 -30,-50 -30,50" transform="translate(285 585) rotate(250)"/>
  </g>

  <g class="stage-labels" filter="url(#label-shadow)">
    <text class="stage-label" transform="translate(555 140) rotate(-8)">STRATEGIZE</text>
    <text class="stage-label" transform="translate(885 262) rotate(52)">TARGET</text>
    <text class="stage-label" transform="translate(880 598) rotate(-56)">ENGAGE</text>
    <text class="stage-label" transform="translate(492 705) rotate(16)">AUTOMATE</text>
    <text class="stage-label" transform="translate(298 382) rotate(-70)">MONETIZE</text>
  </g>

  <g class="cycle-hub">
    <circle cx="605" cy="432" r="215" fill="url(#hub-fill)" filter="url(#soft-shadow)"/>
    <text class="brand-name brand-name--primary" x="605" y="440">BRISK</text>
    <text class="brand-name brand-name--secondary" x="605" y="495">ONLINE MARKETING</text>
  </g>
</svg>
</body>
</html>
```